International Wine Label 202001

Need a wine label designed for several new wines from California being exported to Asia. This label should be focused around an animal theme of the flowing: Tiger, Lion, Horse or Eagle. The label should be adaptable to a product line of wines. For example the label could be used for a Cabernet wine, Merlot, Chardonnay or Pinot. A slight modification to the label design should be incorporated to allow for the different varietals. Front label design only. Can utilize photo image in design.
The label would be around 5.75" x 3.50".

Target Market(s)

25-35 year old wine buyers in the global market

Industry/Entity Type

Retail

Font styles to use
Sans Serif

Requirements
Must have
• Wine name based on design (designer suggest name)
Wine varietals
Vintage date
Additional wording area
Nice to have
• Rectangular label preferred Front label only.

```html
<!DOCTYPE html>
<html lang="en">
<head>
<meta charset="utf-8">
<title>Velmora – Cabernet Sauvignon Labels</title>
<link rel="stylesheet" href="https://fonts.googleapis.com/css2?family=Marcellus&display=swap">
<style>
  :root {
    --backdrop: #e6e7ea;
    --light-paper: #eef0ec;
    --light-ink: #2b2724;
    --light-band: #d8d9d5;
    --light-rule: #9c9d9a;
    --dark-paper: #141110;
    --dark-ink: #f3f1ee;
    --dark-band: #3a3633;
    --dark-rule: #5c5855;
    --tiger-orange: #b9702f;
    --tiger-deep: #6b3c1a;
    --tiger-pale: #d9cbb8;
  }
  * { margin: 0; padding: 0; box-sizing: border-box; }
  html, body { width: 1200px; height: 800px; overflow: hidden; }
  body {
    background: var(--backdrop);
    font-family: "Marcellus", serif;
    display: flex;
    align-items: center;
    justify-content: center;
    gap: 70px;
  }
  .label {
    position: relative;
    width: 400px;
    height: 600px;
    display: flex;
    flex-direction: column;
    align-items: center;
    box-shadow: 0 14px 34px rgba(0,0,0,0.18);
  }
  .label--light { background: var(--light-paper); color: var(--light-ink); }
  .label--dark { background: var(--dark-paper); color: var(--dark-ink); }
  .label__frame {
    position: absolute;
    inset: 14px;
    border: 4px dashed var(--light-rule);
    pointer-events: none;
  }
  .label--dark .label__frame { border-color: var(--dark-rule); }
  .label__name {
    margin-top: 62px;
    font-size: 56px;
    font-weight: 400;
    line-height: 1;
    text-align: center;
    letter-spacing: 3px;
  }
  .label__animal {
    margin-top: 40px;
    width: 300px;
    height: 270px;
    border-radius: 46% 46% 18% 18%;
  }
  .label--light .label__animal {
    background: radial-gradient(ellipse at 50% 40%, var(--tiger-pale) 0%, var(--tiger-orange) 45%, var(--tiger-deep) 75%, rgba(238,240,236,0) 100%);
  }
  .label--dark .label__animal {
    background: radial-gradient(ellipse at 50% 40%, var(--tiger-pale) 0%, var(--tiger-orange) 45%, var(--tiger-deep) 72%, rgba(20,17,16,0) 100%);
  }
  .label__varietal {
    margin-top: 34px;
    width: calc(100% - 28px);
    padding: 8px 0 6px;
    text-align: center;
    font-size: 24px;
    letter-spacing: 0.5px;
  }
  .label--light .label__varietal { background: var(--light-band); }
  .label--dark .label__varietal { background: var(--dark-band); }
  .label__region {
    margin-top: 12px;
    font-size: 24px;
    text-align: center;
    line-height: 1.1;
  }
  .label__vintage { font-size: 24px; text-align: center; line-height: 1.1; }
</style>
</head>
<body>
  <article class="label label--light">
    <div class="label__frame"></div>
    <h1 class="label__name">Velmora</h1>
    <div class="label__animal" role="img" aria-label="Photograph of a resting tiger facing forward"></div>
    <p class="label__varietal">CABERNET SAUVIGNON</p>
    <p class="label__region">NAPA VALLEY</p>
    <p class="label__vintage">2020</p>
  </article>

  <article class="label label--dark">
    <div class="label__frame"></div>
    <h1 class="label__name">Velmora</h1>
    <div class="label__animal" role="img" aria-label="Photograph of a resting tiger facing forward on a dark background"></div>
    <p class="label__varietal">CABERNET SAUVIGNON</p>
    <p class="label__region">NAPA VALLEY</p>
    <p class="label__vintage">2020</p>
  </article>
</body>
</html>
```